Gift voucher for a photo shoot, folding card DIN long (21 x 9.8 cm)

Hello, I'm a professional photographer and need a new design for my gift voucher card for a photo shoot. The design should be applicable to all types of photo shoots (neutral). I prefer a sophisticated design. The folded card should be printed on both sides.
My data should be included: Logo, Address: Wendtaler Gasse 9, 07318 Gera, Email: fotograf@jonasbirkner.eu, Website: www.jonasbirkner.eu Tel.: 0176 / 4389025
Updates

Please design the folding card in DIN long format (105 x 210 mm, landscape format). The card should open horizontally. Please design the front with the words "Gift voucher for you" and my logo. Please make the logo small – the words "Gift voucher" should be in the foreground.
The colors - use elegant gray with gold or white font color.
The inside should contain the words: Photo shoot for ........ worth .....€, as well as my logo.
My contact details should be on the back.

Target Market(s)

Private customer

Colors

Designer to choose only greyscale colors for use in the design.

Requirements
Must have
• Noble appearance, a gift voucher that one likes to give away, words: Gift voucher for you, photo shoot for ..., worth .......€
Nice to have
• Noble appearance of the gift voucher, a gift voucher that you like to give away
Should not have
• no pictures

```html
<!DOCTYPE html>
<html lang="en">
<head>
<meta charset="utf-8">
<title>Gift Voucher – Jonas Birkner</title>
<link rel="stylesheet" href="https://fonts.googleapis.com/css2?family=Cinzel:wght@400;700&family=Montserrat:wght@400;500;600;700&display=swap">
<style>
  :root {
    --stage: #a8a8a8;
    --ink: #050608;
    --paper: #ffffff;
    --silver: #8f8f8f;
    --soft-grey: #7a7a7a;
    --tagline: #6f6f6f;
    --contact: #b5b5b5;
    --text-dark: #111111;
  }
  * { margin: 0; padding: 0; box-sizing: border-box; }
  html, body { width: 1200px; height: 1200px; overflow: hidden; }
  body { background: var(--stage); position: relative; font-family: 'Montserrat', sans-serif; }

  .card { position: absolute; left: 149px; width: 901px; height: 435px; display: flex;
          box-shadow: 0 22px 24px -18px rgba(0,0,0,0.45); }
  .card--outside { top: 128px; }
  .card--inside { top: 642px; height: 434px; flex-direction: column; }

  /* Outside: back panel */
  .back-panel { position: relative; width: 450px; height: 100%; background: var(--ink); overflow: hidden; }
  .monogram-texture { position: absolute; left: 0; top: 0; width: 100%; height: 75%;
          background: linear-gradient(180deg, #1f1f22 0%, #121214 60%, var(--ink) 100%); }
  .contact-icons { position: absolute; top: 267px; left: 0; width: 100%;
          display: flex; justify-content: center; align-items: center; gap: 11px; }
  .contact-icons svg { width: 14px; height: 14px; display: block; }
  .contact-icons .sep { width: 1px; height: 12px; background: var(--paper); }
  .contact-list { position: absolute; top: 294px; left: 0; width: 100%;
          text-align: center; list-style: none; color: var(--contact); font-size: 14px; font-weight: 400; }
  .contact-list li { line-height: 29.3px; }

  /* Outside: front panel */
  .front-panel { position: relative; width: 451px; height: 100%; background: var(--paper); }
  .brand-dot { position: absolute; left: 178px; top: 139px; width: 88px; height: 88px;
          border: 3px solid var(--ink); border-radius: 50%; }
  .brand-name { position: absolute; left: 0; width: 100%; top: 232px; text-align: center;
          font-family: 'Cinzel', serif; font-weight: 400; font-size: 40px; letter-spacing: 1px; color: var(--ink); }
  .brand-tagline { position: absolute; left: 0; width: 100%; top: 279px; text-align: center;
          font-family: 'Montserrat', sans-serif; font-weight: 600; font-size: 15px; letter-spacing: 6px;
          padding-left: 6px; color: var(--tagline); }

  /* Inside */
  .band { height: 173px; background: var(--ink); display: flex; }
  .band-half { position: relative; width: 50%; height: 100%; text-align: center; font-family: 'Cinzel', serif; }
  .band-value { position: absolute; top: 22px; width: 100%; color: var(--paper); font-size: 28px; font-weight: 700; letter-spacing: 0.5px; }
  .band-rule { position: absolute; top: 65px; left: 97px; width: 267px; height: 2px;
          background: linear-gradient(90deg, rgba(255,255,255,0), #ffffff 50%, rgba(255,255,255,0)); }
  .band-title { position: absolute; top: 92px; width: 100%; color: var(--silver); font-size: 52px; font-weight: 700; white-space: nowrap; }
  .enjoy { position: absolute; top: 10px; left: 0; width: 100%; color: var(--paper); font-size: 84px; font-weight: 700; line-height: 1; padding-top: 12px; }
  .present { position: absolute; top: 108px; width: 100%; color: var(--silver); font-size: 37px; font-weight: 700; }

  .sheet { flex: 1; display: flex; background: var(--paper); }
  .sheet-half { position: relative; width: 50%; height: 100%; }
  .sheet-half--right { background: linear-gradient(90deg, #ececec 0%, #ffffff 10%); }
  .session { position: absolute; top: 24px; width: 100%; text-align: center; font-size: 25px; font-weight: 700; color: var(--text-dark); }
  .value-label { position: absolute; top: 108px; left: 169px; width: 120px; height: 30px;
          border-top: 1.5px solid var(--text-dark); border-bottom: 1.5px solid var(--text-dark);
          text-align: center; font-family: 'Cinzel', serif; font-size: 19px; line-height: 27px; color: var(--soft-grey); }
  .value-amount { position: absolute; top: 139px; width: 100%; text-align: center;
          font-family: 'Cinzel', serif; font-weight: 700; font-size: 92px; color: var(--ink); line-height: 1.1; }
  .field { position: absolute; left: 46px; font-size: 25px; font-weight: 500; color: var(--text-dark); }
  .field--to { top: 24px; }
  .field--from { top: 79px; }
  .terms-title { position: absolute; top: 152px; width: 100%; text-align: center; font-size: 14px; font-weight: 600; color: var(--soft-grey); }
  .terms-text { position: absolute; top: 181px; left: 14px; width: 420px; text-align: center;
          font-size: 12.6px; line-height: 16.2px; color: var(--soft-grey); }
</style>
</head>
<body>

<section class="card card--outside">
  <div class="back-panel">
    <div class="monogram-texture" role="img" aria-label="Faint repeating monogram pattern on black"></div>
    <div class="contact-icons">
      <svg viewBox="0 0 14 14" aria-label="Phone"><path fill="#fff" d="M3 1.5l2 .3 1 3-1.3 1a7 7 0 0 0 3.5 3.5l1-1.3 3 1 .3 2c-.2 1-1 1.5-2 1.5A10 10 0 0 1 1.5 3.5c0-1 .5-1.8 1.5-2z"/></svg>
      <span class="sep"></span>
      <svg viewBox="0 0 14 14" aria-label="Website"><g fill="none" stroke="#fff" stroke-width="1.2"><circle cx="7" cy="7" r="5.8"/><ellipse cx="7" cy="7" rx="2.5" ry="5.8"/><path d="M1.2 7h11.6M2 4h10M2 10h10"/></g></svg>
      <span class="sep"></span>
      <svg viewBox="0 0 14 14" aria-label="Email"><rect x="1" y="3" width="12" height="8.5" fill="#fff"/><path d="M1 3l6 5 6-5M1 11.5l4.5-4M13 11.5l-4.5-4" fill="none" stroke="#050608" stroke-width="1"/></svg>
      <span class="sep"></span>
      <svg viewBox="0 0 14 14" aria-label="Address"><g fill="none" stroke="#fff" stroke-width="1.3"><circle cx="7" cy="5" r="2.5"/><path d="M7 7.5v3M2.5 11.5c1-1 8-1 9 0-1 1.2-8 1.2-9 0z"/></g></svg>
    </div>
    <ul class="contact-list">
      <li>0176 / 4389025</li>
      <li>www.jonasbirkner.eu</li>
      <li>fotograf@jonasbirkner.eu</li>
      <li>Wendtaler Gasse 9, 07318 Gera</li>
    </ul>
  </div>
  <div class="front-panel">
    <span class="brand-dot"></span>
    <p class="brand-name">Jonas Birkner</p>
    <p class="brand-tagline">FOTOGRAF</p>
  </div>
</section>

<section class="card card--inside">
  <div class="band">
    <div class="band-half">
      <p class="band-value">Valued in $150</p>
      <span class="band-rule"></span>
      <p class="band-title">A Gift for You</p>
    </div>
    <div class="band-half">
      <p class="enjoy">Enjoy</p>
      <p class="present">Your Present</p>
    </div>
  </div>
  <div class="sheet">
    <div class="sheet-half">
      <p class="session">1 hour photo session</p>
      <p class="value-label">Valued In</p>
      <p class="value-amount">$150</p>
    </div>
    <div class="sheet-half sheet-half--right">
      <p class="field field--to">To:</p>
      <p class="field field--from">From:</p>
      <p class="terms-title">Terms &amp; Conditions</p>
      <p class="terms-text">Lorem ipsum dolor sit amet, consectetur adipiscing elit. Cras euismod sem sem, fermentum pellentesque neque posuere eget. Aenean fringilla vel diam vitae porta.</p>
    </div>
  </div>
</section>

</body>
</html>
```